Webdesign für Energieberatung
Hallo,
es geht um die Erstellung einer Website für einen Diplom Bauingenieur (FH) mit dem Schwerpunkt 'Energieberatung'.
---mit fundierten bauphysikalischen u. technischen Kenntnissen und qualifizierter Ausbildung---
Zu der Thematik - Energieberatung gehören folgende Leistungen.
1. Energetische Beratung und die Erstellung von Energiekonzepten für Bauherren aus dem privaten, gewerblichen und kommunalen Bereichen.
2. Erstellung von energieeffizienten Sanierungsstrategien für Bauherren, die Sanierungsmaßnahmen planen um die energetischen Bilanz ihrer Gebäude zu verbessern mit dem Ziel hier die optimale Lösung erreichen.
3. Bauphysikalische Spezialberechnungen wie z.B. Wärmebrücken-Berechnungen zur Optimierung der EnEV Nachweise oder zur Feststellung von Feuchteproblematiken u. der Durchführung einer Schimmelanalyse.
4. Beratung zu den angebotenen Förderprogrammen zur Energieeinsparung und der Beantragung von öffentlichen Fördermitteln von der ZPT, der DUNO und weitere - wie z.B. regionale Förderer oder Kommunen.
5. Baubegleitung zur Sicherstellung der korrekten Durchführung der festgelegten und berechneten energetischen Werte auf der Baustelle selbst mit abschliessender Qualitätskontrolle und Dokumentation.
6. Ausstellen von Energieausweisen u. die Erstellung von Energiebilanzen für Gewerbe- u. Industriegebäuden (nicht Wohngebäuden) und auch Wohnungen laut den Richtlinien der Energieeinsparverordnung - kurz EnEV und anderen europäischen Richtlinien.
7. Durchführung von bauphysikalischen Messungen wie z.B die Differenzdruckmesssungen- auch Blower-Door Messungen genannt oder die Erstellung von thermografischen Aufnahmen um Schwachstellen z.B. an der Gebäudehülle sichtbar zu machen.
8. Vor - Ort - Betreuung auf der Baustelle in enger Zusammenarbeit mit dem Bauherren, dem Architekten, dem ausführendem Bauunternehmen und weiteren Dienstleistern.
Hier wü..
Aufgabenstellung
Es gibt noch kein Logo...., würden wir aber auch gern haben wollen. Grundsätzlich sind wir offen für alles. Gerne aber im modernen Stil - große Bilder (vielleicht auf Fullscreen) oder auch Videos in Endlosschleife - markante Texte mit schöner Grafik - nicht klein gedacht, sonder ehr sehr selbstbewusst. Auffällig u. neu gedacht - mit dem gewissen i-tüpfelchen. Die Farbe 'orange' darf allerdings nicht vorkommen. Für alles andere sind wir offen. Zu der Bildfrage hatte ich ja bereits oben was geschrieben - würden wir nachliefern. Für geeignete Vorschläge wären wir dankbar.

```html
<!DOCTYPE html>
<html lang="de">
<head>
<meta charset="utf-8">
<title>Hausbilanz – Energieberatung</title>
<link href="https://fonts.googleapis.com/css2?family=Bebas+Neue&family=Open+Sans:wght@400;600&display=swap" rel="stylesheet">
<style>
  :root {
    --white: #ffffff;
    --ink: #2b2b2b;
    --sky: #3fb0e6;
    --navy: #1a4f6e;
    --dark: #121312;
    --heading: 'Bebas Neue', 'Oswald', sans-serif;
    --body: 'Open Sans', Arial, sans-serif;
  }
  * { box-sizing: border-box; margin: 0; padding: 0; }
  html, body { width: 768px; height: 1200px; overflow: hidden; background: var(--white); }
  body { font-family: var(--body); color: var(--white); }

  .section { position: relative; width: 768px; overflow: hidden; }
  .content { position: absolute; left: 134px; z-index: 2; }
  .photo { position: absolute; inset: 0; z-index: 1; }

  /* Hero */
  .hero { height: 380px; }
  .hero .photo {
    background:
      linear-gradient(180deg, rgba(255,255,255,0) 45%, rgba(120,190,80,.55) 100%),
      linear-gradient(115deg, #62c25c 0%, #4fc08a 45%, #3fb3c8 80%, var(--sky) 100%);
  }
  .site-header {
    position: absolute; top: 26px; left: 134px; right: 138px; z-index: 3;
    display: flex; justify-content: space-between; align-items: center;
  }
  .brand { display: flex; align-items: center; gap: 8px; font-family: var(--heading); font-size: 22px; letter-spacing: .5px; }
  .brand-square { width: 16px; height: 16px; border: 2px solid var(--white); }
  .main-nav { display: flex; gap: 13px; font-size: 8px; font-weight: 600; }
  .hero .content { top: 110px; }
  .eyebrow { display: flex; align-items: center; gap: 7px; font-family: var(--heading); font-size: 9.5px; letter-spacing: .3px; }
  .eyebrow::before { content: ""; width: 32px; height: 1px; background: var(--white); }
  .hero-title { font-family: var(--heading); font-weight: 400; font-size: 44px; line-height: .98; margin-top: 10px; letter-spacing: .5px; }
  .hero-rule { width: 252px; height: 2px; background: var(--white); margin: 12px 0 10px; }
  .hero-sub { font-family: var(--heading); font-size: 18px; line-height: 1.15; letter-spacing: .3px; }

  .btn {
    display: inline-flex; align-items: center; gap: 7px;
    border: 1.5px solid var(--white); padding: 6px 22px;
    font-family: var(--heading); font-size: 10.5px; letter-spacing: .4px; color: var(--white);
  }
  .btn svg { width: 10px; height: 8px; }
  .hero .btn { margin-top: 18px; }

  /* Section headings */
  .section-no { font-family: var(--heading); font-size: 10px; width: 38px; border-bottom: 1px solid currentColor; padding-bottom: 2px; }
  .section-title { font-family: var(--heading); font-weight: 400; font-size: 42px; line-height: 1; margin-top: 6px; }
  .section-sub { display: flex; align-items: center; gap: 8px; font-family: var(--heading); font-size: 10px; margin-top: 2px; }
  .section-sub::before { content: ""; width: 34px; height: 1px; background: currentColor; }

  /* Über uns */
  .about { height: 330px; color: var(--ink); }
  .about .photo {
    background: linear-gradient(160deg, #8fd0de 0%, #8fd0b6 35%, #b6e09e 70%, #d9ecc4 100%);
  }
  .portrait {
    position: absolute; right: 0; bottom: 0; width: 330px; height: 330px; z-index: 1;
    background: radial-gradient(ellipse at 60% 55%, #e4ece6 0%, #d6e6d4 45%, rgba(214,230,212,0) 75%);
  }
  .about .content { top: 26px; width: 240px; }
  .about-intro { font-size: 7.6px; line-height: 1.3; margin-top: 12px; }
  .about-columns { display: flex; gap: 12px; margin-top: 9px; font-size: 7.6px; line-height: 1.3; }
  .about-columns p { width: 114px; }
  .about .btn { border-color: var(--white); margin-top: 14px; }

  /* Leistungen */
  .services { height: 350px; }
  .services .photo {
    background:
      linear-gradient(90deg, rgba(20,70,90,.85) 0%, rgba(40,110,90,.5) 45%, rgba(120,180,80,.2) 100%),
      linear-gradient(180deg, var(--navy) 0%, #5e9a5c 40%, #8cc46a 70%, #3d7a4a 100%);
  }
  .services .content { top: 28px; width: 330px; }
  .service-list { list-style: none; margin-top: 12px; }
  .service { display: flex; gap: 9px; margin-bottom: 10px; }
  .service svg { width: 18px; height: 20px; flex: none; margin-top: 1px; }
  .service h3 { font-family: var(--heading); font-weight: 400; font-size: 13px; line-height: 1; letter-spacing: .3px; }
  .service p { font-size: 7px; line-height: 1.3; margin-top: 1px; font-weight: 600; }
  .services .btn { margin-top: 6px; }

  /* Kontakt */
  .contact { height: 140px; }
  .contact .photo { background: linear-gradient(180deg, #1c1f1c 0%, var(--dark) 100%); }
  .contact .content { top: 22px; }
  .contact-title { font-family: var(--heading); font-weight: 400; font-size: 27px; line-height: 1; }
  .contact-rule { width: 22px; height: 2px; background: var(--white); margin: 8px 0 10px; }
  .contact-list { list-style: none; font-size: 8px; font-weight: 600; line-height: 1.3; }
</style>
</head>
<body>

<section class="section hero">
  <div class="photo" role="img" aria-label="Moderne Villa am Hang mit grünem bis blauem Farbverlauf"></div>
  <header class="site-header">
    <div class="brand"><span class="brand-square"></span>HAUSBILANZ</div>
    <nav class="main-nav"><span>Über uns</span><span>Leistungen</span><span>Preise</span><span>Kontakt</span></nav>
  </header>
  <div class="content">
    <p class="eyebrow">Bauphysikalische und technische Kenntnisse</p>
    <h1 class="hero-title">Energetische<br>Beratung und<br>Energiekonzepte</h1>
    <div class="hero-rule"></div>
    <p class="hero-sub">Fundierte bauphysikalische<br>und technische Kenntnisse</p>
    <span class="btn"><svg viewBox="0 0 10 8"><path d="M0 4h9M6 1l3 3-3 3" fill="none" stroke="#fff" stroke-width="1"/></svg>Leistungen</span>
  </div>
</section>

<section class="section about">
  <div class="photo"></div>
  <div class="portrait" role="img" aria-label="Porträtfoto des Energieberaters"></div>
  <div class="content">
    <p class="section-no">01</p>
    <h2 class="section-title">Über uns</h2>
    <p class="section-sub">Bauphysik Blindtext</p>
    <p class="about-intro">Weit hinten, hinter den Wortbergen, fern der Länder Vokalien und Konsonantien leben die Blindtexte. Abgeschieden wohnen sie in Buchstabhausen.</p>
    <div class="about-columns">
      <p>Weit hinten, hinter den Wortbergen, fern der Länder Vokalien und Konsonantien leben die Blindtexte. Abgeschieden wohnen sie in Buchstabhausen an der Küste des Semantik, eines großen Sprachozeans. Ein kleines Bächlein namens Duden fließt durch ihren Ort und versorgt sie mit den nötigen Regelialien. Es ist ein paradiesma-</p>
      <p>tisches Land, in dem einem gebratene Satzteile in den Mund fliegen. Nicht einmal von der allmächtigen Interpunktion werden die Blindtexte beherrscht – ein geradezu unorthographisches Leben. Eines Tages aber beschloß eine kleine Zeile Blindtext, ihr Name war Lorem Ipsum, hinaus zu gehen in die weite Grammatik.</p>
    </div>
    <span class="btn"><svg viewBox="0 0 10 8"><path d="M0 4h9M6 1l3 3-3 3" fill="none" stroke="#fff" stroke-width="1"/></svg>Mehr erfahren</span>
  </div>
</section>

<section class="section services">
  <div class="photo" role="img" aria-label="Modernes Mehrfamilienhaus mit Balkonen und Bäumen in Grüntönen"></div>
  <div class="content">
    <p class="section-no">02</p>
    <h2 class="section-title">Leistungen</h2>
    <p class="section-sub">Bauphysik Blindtext</p>
    <ul class="service-list">
      <li class="service">
        <svg viewBox="0 0 18 20" fill="none" stroke="#fff" stroke-width="1"><path d="M9 1a6 6 0 0 0-3.5 10.9V14h7v-2.1A6 6 0 0 0 9 1z"/><path d="M6 16h6M7 18h4"/></svg>
        <div><h3>Energetische Beratung</h3><p>und die Erstellung von Energiekonzepten für Bauherren aus<br>dem privaten, gewerblichen und kommunalen Bereichen</p></div>
      </li>
      <li class="service">
        <svg viewBox="0 0 18 20" fill="none" stroke="#fff" stroke-width="1"><path d="M9 2c-2 3-3 4.5-3 6a3 3 0 0 0 6 0c0-1.5-1-3-3-6z"/><path d="M4 11c-1.5 2-2 3-2 4a2 2 0 0 0 4 0c0-1-.5-2-2-4z"/><path d="M14 11c-1.5 2-2 3-2 4a2 2 0 0 0 4 0c0-1-.5-2-2-4z"/></svg>
        <div><h3>Energieeffiziente Sanierungsstrategien</h3><p>für Bauherren, die Sanierungsmaßnahmen planen um die<br>energetischen Bilanz ihrer Gebäude zu verbessern</p></div>
      </li>
      <li class="service">
        <svg viewBox="0 0 18 20" fill="none" stroke="#fff" stroke-width="1"><path d="M1 19h16M2 19V9h5v10M7 19V3h6v16M13 19v-8h4v8"/><path d="M9 6h2M9 9h2M9 12h2M4 12h1M4 15h1"/></svg>
        <div><h3>Bauphysikalische Spezialberechnungen</h3><p>wie z.B. Wärmebrücken-Berechnungen zur Optimierung der EnEV<br>Nachweise oder zur Feststellung von Feuchteproblematiken</p></div>
      </li>
      <li class="service">
        <svg viewBox="0 0 18 20" fill="none" stroke="#fff" stroke-width="1"><path d="M11 2c-3 2-4 4-3 7 3 0 5-3 3-7z"/><path d="M1 15l4-2h4l3 1-3 1M1 18l5 1 7-2 4-4"/></svg>
        <div><h3>Beratung zu den Förderprogrammen</h3><p>zur Energieeinsparung und der Beantragung von öffentlichen<br>Fördermitteln von der ZPT, der DUNO und weitere</p></div>
      </li>
    </ul>
    <span class="btn"><svg viewBox="0 0 10 8"><path d="M0 4h9M6 1l3 3-3 3" fill="none" stroke="#fff" stroke-width="1"/></svg>Ganzes Angebot</span>
  </div>
</section>

<section class="section contact">
  <div class="photo" role="img" aria-label="Dunkles Foto einer Hausfassade bei Nacht"></div>
  <div class="content">
    <h2 class="contact-title">Kontakt</h2>
    <div class="contact-rule"></div>
    <ul class="contact-list">
      <li>Vorname Nachname</li>
      <li>Adresse</li>
      <li>Telefon</li>
      <li>E-Mail</li>
    </ul>
  </div>
</section>

</body>
</html>
```